Criação de Papelaria Profissional para Construção & Engenharia
" Administração de obras: o cliente nos contrata para realizar a gestão da construção de sua casa (alto padrão), desde orçamentos, cronograma de obra, acompanhamento da obra e gestão da mão de obra. Desenvolvimento de novos negócios: Realizamos o estudo de viabilidade técnico-econômica de terrenos para realização de loteamentos, condomínios e empreendimentos verticais e prospectamos construtoras e loteadoras para apresentar o projeto. Gestão de Grupos de investimentos: Fracionamos investimentos do setor imobiliário em cotas para acelerar um determinado negócio. Ex: adquirimos um lote em condomínio, realizamos um projeto de casa alto padrão e calculamos o custo total entre terreno e obra. Fracionamos em contas de 50 mil e vendemos para arrecadar o valor total do investimento. Assim, construimos a casa e na hora da sua venda é dividido os lucros proporcionalmente as cotas adquiridas. "

```html
<!DOCTYPE html>
<html lang="pt-BR">
<head>
<meta charset="utf-8">
<title>Verta Engenharia — Envelope</title>
<link rel="stylesheet" href="https://fonts.googleapis.com/css2?family=Montserrat:wght@400;600;700&display=swap">
<style>
  :root{
    --board:#dcdcdc;
    --navy:#14304f;
    --navy-deep:#0f2740;
    --gold:#b99a5e;
    --paper:#ffffff;
    --ink:#3a4450;
  }
  *{margin:0;padding:0;box-sizing:border-box}
  html,body{width:1200px;height:1200px;overflow:hidden}
  body{background:var(--board);font-family:"Montserrat",sans-serif;position:relative}
  .board-frame{position:absolute;left:0;top:0}
  .board-label{position:absolute;top:26px;left:0;width:1200px;text-align:center;
    font-weight:700;font-size:30px;letter-spacing:1px;color:var(--navy-deep)}
  .envelope-front{position:absolute;left:192px;top:108px;width:811px;height:415px;background:var(--navy);overflow:hidden}
  .front-decor{position:absolute;right:0;top:0;width:330px;height:380px;
    background:linear-gradient(200deg,rgba(255,255,255,.08),rgba(255,255,255,0) 70%)}
  .front-stripe{position:absolute;left:0;top:381px;width:100%;height:8px;background:var(--gold)}
  .brand{display:flex;align-items:center;justify-content:center;gap:14px;
    font-weight:600;letter-spacing:4px;text-transform:uppercase;text-align:center;line-height:1.15}
  .brand-dot{width:22px;height:22px;border-radius:50%;background:currentColor;flex:none}
  .front-brand{position:absolute;left:0;top:165px;width:100%;color:var(--paper);font-size:44px}
  .envelope-back{position:absolute;left:192px;top:557px;width:811px;height:403px;background:var(--paper)}
  .back-flap{position:absolute;left:0;top:0}
  .back-brand{position:absolute;left:0;top:170px;width:100%;color:var(--navy);font-size:40px}
  .contact-row{position:absolute;left:0;bottom:30px;width:100%;display:flex;justify-content:space-around;
    align-items:center;font-size:12px;color:var(--ink);padding:0 20px}
  .contact-item{display:flex;align-items:center;gap:6px}
  .contact-item svg{flex:none}
  .bottom-brand{position:absolute;left:0;top:1040px;width:1200px;color:var(--navy);font-size:56px}
</style>
</head>
<body>
  <svg class="board-frame" width="1200" height="1200" viewBox="0 0 1200 1200" aria-hidden="true">
    <path d="M430 38 H100 Q53 38 53 85 V1128" fill="none" stroke="var(--navy)" stroke-width="6"/>
    <path d="M770 38 H1100 Q1147 38 1147 85 V1128" fill="none" stroke="var(--navy)" stroke-width="6"/>
  </svg>
  <div class="board-label">ENVELOPE</div>

  <section class="envelope-front">
    <div class="front-decor" role="img" aria-label="Faint decorative brand symbol"></div>
    <div class="brand front-brand"><span class="brand-dot"></span><span>Verta<br>Engenharia</span></div>
    <div class="front-stripe"></div>
  </section>

  <section class="envelope-back">
    <svg class="back-flap" width="811" height="120" viewBox="0 0 811 120" aria-hidden="true">
      <path d="M0 0 H811 V40 Q811 70 780 78 L640 92 Q405 112 170 92 L31 78 Q0 70 0 40 Z" fill="var(--navy)"/>
    </svg>
    <div class="brand back-brand"><span class="brand-dot"></span><span>Verta<br>Engenharia</span></div>
    <div class="contact-row">
      <span class="contact-item">
        <svg width="14" height="14" viewBox="0 0 14 14"><path d="M3 1 L5 4 L4 5.5 Q5.5 8.5 8.5 10 L10 9 L13 11 L11.5 13 Q5 12.5 1 3 Z" fill="var(--ink)"/></svg>
        (12) 3000-4410</span>
      <span class="contact-item">
        <svg width="15" height="11" viewBox="0 0 15 11"><rect x="0.5" y="0.5" width="14" height="10" fill="none" stroke="var(--ink)"/><path d="M0.5 0.5 L7.5 6 L14.5 0.5" fill="none" stroke="var(--ink)"/></svg>
        contato@verta.com.br</span>
      <span class="contact-item">
        <svg width="13" height="13" viewBox="0 0 13 13"><rect width="13" height="13" rx="2" fill="var(--ink)"/></svg>
        /vertaengenharia</span>
      <span class="contact-item">
        <svg width="13" height="13" viewBox="0 0 13 13"><circle cx="6.5" cy="6.5" r="6.5" fill="var(--ink)"/></svg>
        @vertaeng</span>
      <span class="contact-item">
        <svg width="12" height="16" viewBox="0 0 12 16"><path d="M6 15 Q1 9 1 6 A5 5 0 0 1 11 6 Q11 9 6 15 Z" fill="none" stroke="var(--ink)" stroke-width="1.4"/><circle cx="6" cy="6" r="1.8" fill="var(--ink)"/></svg>
        R. das Acácias, 120<br>Taubaté SP</span>
    </div>
  </section>

  <div class="brand bottom-brand"><span class="brand-dot"></span><span>Verta<br>Engenharia</span></div>
</body>
</html>
```